Business Card Design using new attached logo

We are a family run Plumbing and Heating firm looking to improve our company image with an improved business card and new logo.We are looking to keep the company colour (Blue) involved in our design

Reason: New logo added which needs to be incorporated on designs

Industry/Entity Type

Business

Contact Information for Business Card

See attachment of all info required.

Requirements
Must have
• We have just picked a new company logo which is attached.
• Could you please provide your business card designs using this logo.
• We are looking for the logo on the back as well as the front with all the info required

```html
<!DOCTYPE html>
<html lang="en">
<head>
<meta charset="utf-8">
<title>Kestrel Heating Ltd – Business Card</title>
<link rel="stylesheet" href="https://fonts.googleapis.com/css2?family=Noto+Serif:wght@400;700&display=swap">
<style>
  :root {
    --brand-blue: #0d66a3;
    --ink: #2b2b2b;
    --slate: #7b7f84;
    --paper: #ffffff;
    --backdrop: #d9dadb;
  }
  * { box-sizing: border-box; margin: 0; padding: 0; }
  html, body { width: 1200px; height: 1000px; overflow: hidden; }
  body {
    background: var(--backdrop);
    font-family: "Noto Serif", Georgia, serif;
    color: var(--ink);
    position: relative;
  }
  .card {
    position: absolute;
    left: 280px;
    width: 640px;
    height: 380px;
    background: var(--paper);
    box-shadow: 0 6px 20px rgba(0,0,0,0.18);
    overflow: hidden;
  }
  .card--front { top: 70px; }
  .card--back  { top: 540px; }
  .card__band {
    position: absolute; left: 0; right: 0; bottom: 0;
    height: 26px; background: var(--brand-blue);
  }
  .card--back .card__band { height: 10px; }
  .card__rules { position: absolute; inset: 0; }
  .brand {
    position: absolute;
    display: flex; align-items: center; gap: 12px;
    color: var(--brand-blue);
    font-weight: 700;
    white-space: nowrap;
  }
  .brand__mark { background: var(--brand-blue); flex: none; }
  .card--front .brand { left: 40px; top: 44px; font-size: 30px; line-height: 40px; }
  .card--front .brand__mark { width: 28px; height: 28px; }
  .card--back .brand {
    left: 0; right: 0; top: 150px; justify-content: center; font-size: 42px;
  }
  .card--back .brand__mark { width: 38px; height: 38px; }
  .person {
    position: absolute; right: 34px; top: 84px; text-align: right;
  }
  .person__name {
    font-size: 20px; line-height: 26px; font-weight: 700;
    letter-spacing: 0.5px; color: var(--ink);
  }
  .person__role {
    font-size: 15px; line-height: 20px; color: var(--brand-blue);
    margin-top: 14px;
  }
  .contacts {
    position: absolute; left: 40px; top: 214px;
    list-style: none; font-size: 15.5px; line-height: 21px;
  }
  .contacts li { display: flex; align-items: flex-start; gap: 10px; }
  .contacts svg { width: 14px; height: 14px; margin-top: 4px; flex: none; fill: var(--brand-blue); }
</style>
</head>
<body>

<section class="card card--front" aria-label="Card front">
  <svg class="card__rules" viewBox="0 0 640 380" aria-hidden="true">
    <polyline points="34,202 330,202 400,150 520,150" fill="none" stroke="#0d66a3" stroke-width="4"/>
    <polyline points="410,124 424,116 606,116" fill="none" stroke="#7b7f84" stroke-width="5"/>
  </svg>

  <div class="brand"><span class="brand__mark"></span><span class="brand__name">Kestrel Heating Ltd</span></div>

  <div class="person">
    <p class="person__name">MARTIN HALE</p>
    <p class="person__role">Director</p>
  </div>

  <ul class="contacts">
    <li><svg viewBox="0 0 16 16"><path d="M2 5c0-2 2-3 6-3s6 1 6 3v1h-3V5H5v1H2zM4 7h8l2 7H2z"/></svg>020 7946 0321</li>
    <li><svg viewBox="0 0 16 16"><path d="M4 1h8v14H4zM5.5 3v9h5V3z"/></svg>077 00 900412</li>
    <li><svg viewBox="0 0 16 16"><path d="M2 6h12v8H2zM4 2h8v3H4z"/></svg>020 7946 0874</li>
    <li><svg viewBox="0 0 16 16"><path d="M1 3h14v10H1zM2.5 4.5 8 9l5.5-4.5z" fill-rule="evenodd"/></svg>martinhale@kestrelheating.co.uk</li>
    <li><svg viewBox="0 0 16 16"><path d="M8 1a5 5 0 0 1 5 5c0 4-5 9-5 9S3 10 3 6a5 5 0 0 1 5-5zm0 3a2 2 0 1 0 0 4 2 2 0 0 0 0-4z"/></svg>Orchard Lane, Brampton<br>Kent BR9 2XY</li>
  </ul>

  <div class="card__band"></div>
</section>

<section class="card card--back" aria-label="Card back">
  <div class="brand"><span class="brand__mark"></span><span class="brand__name">Kestrel Heating Ltd</span></div>
  <div class="card__band"></div>
</section>

</body>
</html>
```